Medical Eye Care Practice needs a unique business card design.

I need a business card for my medical, eye care practice. I am seeking a unique design, possibly with a vertical or atypical shape layout -- something to make the card stand out. I would like the final design to communicate health and wellness with a contemporary feel. Please incorporate my logo and slogan with a color scheme based off of my logo. It should also identify all of the information that is listed on my sample business card. The back side should be utilized for appointment reminder with date, time, and room for notes. I would also like some incorporation of facebook, twitter, and google plus links.

```html
<!DOCTYPE html>
<html lang="en">
<head>
<meta charset="utf-8">
<title>Clearwater Eye Health &amp; Wellness – Business Card</title>
<link rel="stylesheet" href="https://fonts.googleapis.com/css2?family=Montserrat:wght@400;500;600&family=Open+Sans:wght@400;600&display=swap">
<style>
  :root {
    --bg-top: #f2f2f2;
    --bg-bottom: #c9c9c9;
    --card-white: #ffffff;
    --brown: #7d6c4d;
    --brown-dark: #574a32;
    --brown-light: #a8976f;
    --green: #8db43c;
    --ink: #4c4c4c;
    --rule: #b9ae97;
    --strip: #d9d3c4;
  }
  * { margin: 0; padding: 0; box-sizing: border-box; }
  html, body { width: 1200px; height: 873px; overflow: hidden; }
  body {
    background: linear-gradient(var(--bg-top), var(--bg-bottom));
    font-family: "Open Sans", Arial, sans-serif;
    position: relative;
  }
  .card {
    position: absolute;
    top: 286px;
    width: 520px;
    height: 300px;
    box-shadow: 0 8px 22px rgba(0,0,0,.28);
    overflow: hidden;
  }
  /* Front */
  .card-front { left: 60px; background: var(--card-white); }
  .brand { position: absolute; left: 30px; top: 42px; display: flex; align-items: center; gap: 12px; }
  .brand-dot { width: 30px; height: 30px; border-radius: 50%; background: var(--green); }
  .brand-name {
    font-family: "Montserrat", Arial, sans-serif;
    font-weight: 600;
    color: var(--brown);
    line-height: 1.15;
  }
  .brand-name .line-main { display: block; font-size: 26px; letter-spacing: 1px; }
  .brand-name .line-sub { display: block; font-size: 10.5px; letter-spacing: 1.2px; }
  .person {
    position: absolute; left: 26px; right: 26px; top: 184px;
    border-bottom: 1.5px solid var(--rule);
    padding-bottom: 3px;
    display: flex; justify-content: space-between; align-items: flex-end;
  }
  .person-name { font-family: "Montserrat", Arial, sans-serif; font-size: 13px; font-weight: 600; color: var(--brown); }
  .person-name .credentials { font-weight: 400; font-size: 10px; color: var(--green); margin-left: 4px; }
  .social { display: flex; gap: 4px; }
  .social span { width: 10px; height: 10px; background: var(--brown-light); border-radius: 2px; }
  .contact { position: absolute; top: 212px; left: 28px; right: 26px; display: flex; gap: 22px; font-size: 10.5px; color: var(--green); }
  .contact-group { display: flex; gap: 7px; align-items: flex-start; }
  .contact-group svg { flex: none; margin-top: 2px; }
  .contact-group b { color: var(--brown); font-weight: 600; }
  .divider { width: 1px; height: 28px; background: var(--rule); }
  .front-strip { position: absolute; left: 0; right: 0; bottom: 0; height: 8px; background: var(--brown); }
  .front-tab {
    position: absolute; left: 90px; width: 290px; bottom: 8px; height: 30px;
    background: var(--brown);
    color: #fff; text-align: center;
    font-size: 7.5px; letter-spacing: 1.4px; line-height: 1.5; padding-top: 5px;
  }
  /* Back */
  .card-back {
    left: 620px;
    background: radial-gradient(circle at 47% 40%, #c8b58e 0%, #9a8560 22%, var(--brown) 48%, var(--brown-dark) 100%);
    color: #fff;
  }
  .appointment-title { position: absolute; top: 26px; width: 100%; text-align: center; font-family: "Montserrat", Arial, sans-serif; font-size: 21px; font-weight: 500; }
  .field { position: absolute; font-size: 12px; display: flex; align-items: flex-end; }
  .field .line { border-bottom: 1px solid rgba(255,255,255,.55); margin-left: 6px; height: 14px; }
  .field-date { left: 26px; top: 82px; }
  .field-date .line { width: 120px; }
  .field-time { left: 290px; top: 82px; }
  .field-time .line { width: 160px; }
  .field-reason { left: 26px; top: 128px; }
  .field-reason .line { width: 334px; }
  .notes-line { position: absolute; left: 26px; right: 40px; top: 172px; border-bottom: 1px solid rgba(255,255,255,.45); }
  .back-contact { position: absolute; bottom: 28px; width: 100%; text-align: center; font-size: 10.5px; line-height: 1.35; }
  .back-strip { position: absolute; left: 0; right: 0; bottom: 0; height: 8px; background: var(--strip); }
</style>
</head>
<body>
  <section class="card card-front" aria-label="Business card front">
    <div class="brand">
      <span class="brand-dot"></span>
      <div class="brand-name">
        <span class="line-main">CLEARWATER</span>
        <span class="line-sub">EYE HEALTH &amp; WELLNESS</span>
      </div>
    </div>

    <div class="person">
      <p class="person-name">Dana Hollis<span class="credentials">OD, FAAO</span></p>
      <div class="social" aria-label="Social links"><span></span><span></span><span></span></div>
    </div>

    <div class="contact">
      <div class="contact-group">
        <svg width="12" height="12" viewBox="0 0 24 24" aria-hidden="true"><path fill="#7d6c4d" d="M6.6 10.8a15 15 0 0 0 6.6 6.6l2.2-2.2a1 1 0 0 1 1-.25 11.4 11.4 0 0 0 3.6.57 1 1 0 0 1 1 1V20a1 1 0 0 1-1 1A17 17 0 0 1 3 4a1 1 0 0 1 1-1h3.5a1 1 0 0 1 1 1c0 1.25.2 2.45.57 3.6a1 1 0 0 1-.25 1z"/></svg>
        <p><b>T:</b> (555) 014-2210<br><b>F:</b> (555) 014-2211</p>
      </div>
      <span class="divider"></span>
      <div class="contact-group">
        <svg width="12" height="12" viewBox="0 0 24 24" aria-hidden="true"><path fill="#7d6c4d" d="M12 3 2 12h3v8h5v-5h4v5h5v-8h3z"/></svg>
        <p>418 Harbor Rd. Suite 210<br>BROOKFIELD, ST 00000</p>
      </div>
    </div>

    <div class="front-tab">
      <p>FOR VISION · FOR HEALTH · FOR LIFE</p>
      <p>www.clearwater-eye.example</p>
    </div>
    <div class="front-strip"></div>
  </section>

  <section class="card card-back" aria-label="Business card back, appointment reminder">
    <h2 class="appointment-title">Appointment</h2>
    <div class="field field-date">Date:<span class="line"></span></div>
    <div class="field field-time">Time:<span class="line"></span></div>
    <div class="field field-reason">Reason for visit:<span class="line"></span></div>
    <div class="notes-line"></div>
    <p class="back-contact">www.clearwater-care.example<br>(555) 014-2290</p>
    <div class="back-strip"></div>
  </section>
</body>
</html>
```